Design a Flyer for Author "Darnel Whitcombe"

Using pictures provided (you can choose to use one or 3 images). Create a (Flyer Design) for promotion of website.

Using creative placement of words and lettering, please create a flyer with below information. Please be creative and unique with the fonts/styling of lettering.

Author’s name should be strategically place around image (Preferably on the right hand side of image towards the top of page):
Author’s Name: Darnel Whitcombe “The Gentle Giant of Letters”.

A misty image of a rose or a transparent image of a rose needs to be strategically placed under the name of author or transparent behind the author’s name. Website name needs to be near bottom and centered.

Author’s website: www.darnelwhitcombe.example

FINAL NOTES: Please ensure that the rose image is transparent not the solid picture. The background color can be solid white, misty colored charcoal or any color that fits with images, be creative with the background colors.

Letters need to be dark grey or charcoal/color of suit.

Example shots are provided.
Images are provided.

WORK MUST BE GOOD QUALITY, HIGH DEFINTION.

```html
<!DOCTYPE html>
<html lang="en">
<head>
<meta charset="utf-8">
<title>Darnel Whitcombe — The Gentle Giant of Letters</title>
<link rel="stylesheet" href="https://fonts.googleapis.com/css2?family=Pinyon+Script&family=Archivo+Narrow:wght@700&family=Archivo+Black&display=swap">
<style>
  :root {
    --mist-white: #f4f8f1;
    --mist-green: #d3e8c9;
    --mist-green-deep: #aed3a1;
    --rose-red: #d8585a;
    --rose-mid: #e58c88;
    --rose-pink: #f2c2be;
    --suit-light: #e4dccb;
    --suit-beige: #d4c8b1;
    --suit-shadow: #b3a68f;
    --shirt-blue: #6f9fd8;
    --charcoal: #2f2a26;
    --band-green: #4fae54;
    --band-green-light: #b8e3ad;
    --band-green-dark: #1f6e2b;
    --band-text: #b6e04a;
    --band-outline: #0d2a10;
    --url-fill: #dbe6f2;
    --url-outline: #0f1c33;
  }
  html, body {
    margin: 0;
    padding: 0;
    overflow: hidden;
    background: #ffffff;
  }
  .flyer {
    position: relative;
    width: 1200px;
    height: 900px;
    overflow: hidden;
    background:
      radial-gradient(ellipse at 88% 55%, var(--mist-white) 0%, transparent 50%),
      radial-gradient(ellipse at 8% 12%, var(--mist-green-deep) 0%, transparent 45%),
      radial-gradient(ellipse at 95% 92%, var(--mist-green-deep) 0%, transparent 40%),
      linear-gradient(135deg, var(--mist-green) 0%, var(--mist-white) 55%, var(--mist-green) 100%);
  }
  .rose {
    position: absolute;
    left: 630px;
    top: 55px;
    width: 490px;
    height: 430px;
    border-radius: 46% 54% 50% 50% / 48% 46% 54% 52%;
    background:
      radial-gradient(ellipse at 55% 38%, var(--rose-red) 0%, var(--rose-mid) 35%, var(--rose-pink) 62%, rgba(242,194,190,0) 78%);
    opacity: 0.72;
  }
  .author-portrait {
    position: absolute;
    left: 0;
    top: 0;
    width: 760px;
    height: 900px;
    background:
      linear-gradient(100deg, var(--suit-light) 0%, var(--suit-beige) 45%, var(--suit-shadow) 80%, rgba(179,166,143,0) 100%),
      linear-gradient(180deg, var(--shirt-blue) 0%, var(--suit-beige) 40%);
    background-blend-mode: multiply;
    -webkit-mask-image: linear-gradient(90deg, #000 70%, transparent 100%);
    mask-image: linear-gradient(90deg, #000 70%, transparent 100%);
    opacity: 0.85;
  }
  .author-name {
    position: absolute;
    left: 618px;
    top: 28px;
    margin: 0;
    font-family: "Pinyon Script", cursive;
    font-weight: 400;
    font-size: 124px;
    line-height: 1.1;
    color: var(--charcoal);
    text-shadow: 2px 2px 0 #ffffff, 4px 5px 6px rgba(0,0,0,0.35);
  }
  .author-name .first { display: block; }
  .author-name .last { display: block; padding-left: 30px; }
  .tagline-band {
    position: absolute;
    left: 557px;
    top: 483px;
    width: 603px;
    height: 72px;
    display: flex;
    align-items: center;
    justify-content: flex-end;
    padding-right: 6px;
    box-sizing: border-box;
    background: linear-gradient(180deg, var(--band-green-light) 0%, var(--band-green) 45%, var(--band-green-dark) 100%);
    border-left: 14px solid var(--band-green);
  }
  .tagline {
    margin: 0;
    font-family: "Archivo Narrow", sans-serif;
    font-weight: 700;
    font-size: 34px;
    letter-spacing: 0.5px;
    word-spacing: 6px;
    color: var(--band-text);
    text-shadow: 1px 1px 0 var(--band-outline), -1px -1px 0 var(--band-outline), 1px -1px 0 var(--band-outline), -1px 1px 0 var(--band-outline);
  }
  .website {
    position: absolute;
    left: 0;
    right: 0;
    top: 800px;
    margin: 0;
    text-align: center;
    font-family: "Archivo Black", sans-serif;
    font-size: 56px;
    letter-spacing: 1px;
    color: var(--url-fill);
    -webkit-text-stroke: 2px var(--url-outline);
    text-shadow: 3px 4px 5px rgba(0,0,0,0.45);
  }
</style>
</head>
<body>
  <main class="flyer">
    <div class="rose" role="img" aria-label="Transparent misty red rose behind the author's name"></div>
    <div class="author-portrait" role="img" aria-label="Seated portrait of the author in a light beige three-piece suit, blue shirt and striped tie"></div>
    <h1 class="author-name"><span class="first">Darnel</span><span class="last">Whitcombe</span></h1>
    <div class="tagline-band"><p class="tagline">The Gentle Giant of Letters</p></div>
    <p class="website">www.darnelwhitcombe.example</p>
  </main>
</body>
</html>
```